Residential improvers, A Cozy Perch 2 Go *

Cozy Perch 2 Go is a real estate company specializing in turning unloved properties into improved, happy places to live. We specialize in thoughtfully-improved residential properties for buyers or renters. Our company needs a business card that reflects the renovated homes we create using green and Feng Shui principles,

Please disregard the images we submitted. We are looking for an abstract, sophisticated elegant design. No eggs in a nest ... nothing cute. The image can be soft.
Updates

Aloha (hello) all designers. We are a serious property investment/improvement company. We strive to be unique, renovating with style and elegance. Our business card must portray the same message. We thought the nest and flower might be "it" ... clearly it's not, once we saw what you submitted. Please revisit the brief as it was modified yesterday. Mahalo for your input! We look forward to hearing from all designers that have been invited.

Industry/Entity Type

Real Estate Development

Contact Information for Business Card

We will have separate business cards for
1) Corabeth Lindqvist 808-555-0173 corabeth@mailbrook.test
2) Marla Fenwright 808-555-0198 marlafenwright@mailbrook.test
** can we add the website later ... in the process of approval.
Investors * Renovators * Connectors

Font styles to use
Sans Serif

Colors
cadf82

Requirements
Must have
• a feng shui feel ... modern. Color - green with black print.
Nice to have
• A Cozy Perch 2 Go

```html
<!DOCTYPE html>
<html lang="en">
<head>
<meta charset="utf-8">
<title>Cozy Perch 2 Go — Business Card</title>
<link href="https://fonts.googleapis.com/css2?family=Questrial&family=Montserrat:wght@700&display=swap" rel="stylesheet">
<style>
  :root {
    --canvas: #ffffff;
    --leaf: #cadf82;
    --ink: #000000;
    --paper: #ffffff;
  }
  * { box-sizing: border-box; margin: 0; padding: 0; }
  html, body {
    width: 1000px; height: 1200px; overflow: hidden;
    background: var(--canvas);
  }
  .stage { position: relative; width: 1000px; height: 1200px; }

  .card {
    position: absolute; top: 160px; width: 420px; height: 698px;
    font-family: "Questrial", sans-serif;
  }
  .card--front { left: 51px; background: var(--leaf); color: var(--ink); }
  .card--back { left: 532px; background: var(--ink); color: var(--paper); }

  /* brand name set in plain type */
  .brand {
    position: absolute; left: 0; right: 0;
    display: flex; align-items: center; justify-content: center; gap: 14px;
    font-family: "Questrial", sans-serif; font-weight: 400;
    font-size: 40px; line-height: 1.05; letter-spacing: -0.5px;
  }
  .brand__mark { width: 22px; height: 22px; flex: none; }
  .card--front .brand { top: 340px; color: var(--ink); }
  .card--front .brand__mark { background: var(--ink); }
  .card--back .brand { top: 128px; color: var(--paper); }
  .card--back .brand__mark { background: var(--leaf); border-radius: 50%; }

  .site {
    position: absolute; left: 0; right: 0; top: 631px;
    text-align: center; font-size: 21px; letter-spacing: 0.3px;
  }
  .site strong { font-family: "Montserrat", sans-serif; font-weight: 700; font-size: 19px; }

  .name-tab {
    position: absolute; left: 0; top: 396px;
    width: 332px; height: 104px;
    background: var(--paper); color: var(--ink);
    border-radius: 0 52px 52px 0;
    padding: 22px 0 0 46px;
  }
  .name-tab__first {
    font-family: "Montserrat", sans-serif; font-weight: 700;
    font-size: 31px; line-height: 1; letter-spacing: 0.5px;
  }
  .name-tab__last { font-size: 29px; line-height: 1; margin-top: 1px; }

  .contacts { position: absolute; left: 50px; top: 514px; list-style: none; }
  .contacts li {
    display: flex; align-items: center; gap: 16px;
    height: 29px; font-size: 19px; letter-spacing: 0.4px;
  }
  .contacts svg { width: 20px; height: 20px; flex: none; }
  .icon { fill: none; stroke: var(--leaf); stroke-width: 1.8; }
  .icon--solid { fill: var(--leaf); stroke: none; }
</style>
</head>
<body>
<main class="stage">

  <section class="card card--front" aria-label="Card front">
    <div class="brand"><span class="brand__mark"></span><span>Cozy Perch 2 Go</span></div>
    <p class="site">www.<strong>cozyperch2go</strong>.test</p>
  </section>

  <section class="card card--back" aria-label="Card back">
    <div class="brand"><span class="brand__mark"></span><span>Cozy Perch 2 Go</span></div>

    <div class="name-tab">
      <p class="name-tab__first">Corabeth</p>
      <p class="name-tab__last">Lindqvist</p>
    </div>

    <ul class="contacts">
      <li>
        <svg viewBox="0 0 20 20" aria-hidden="true">
          <rect class="icon" x="6" y="2" width="8" height="16" rx="1.5"/>
          <rect class="icon--solid" x="8" y="5" width="4" height="4"/>
          <circle class="icon--solid" cx="10" cy="14.5" r="1.2"/>
        </svg>
        <span>808-555-0173</span>
      </li>
      <li>
        <svg viewBox="0 0 20 20" aria-hidden="true">
          <rect class="icon" x="2" y="4.5" width="16" height="11"/>
          <polyline class="icon" points="2,4.5 10,11 18,4.5"/>
        </svg>
        <span>corabeth@mailbrook.test</span>
      </li>
      <li>
        <svg viewBox="0 0 20 20" aria-hidden="true">
          <circle class="icon" cx="10" cy="10" r="8"/>
          <ellipse class="icon" cx="10" cy="10" rx="3.5" ry="8"/>
          <line class="icon" x1="2" y1="10" x2="18" y2="10"/>
          <line class="icon" x1="10" y1="2" x2="10" y2="18"/>
        </svg>
        <span>www.cozyperch2go.test</span>
      </li>
    </ul>
  </section>

</main>
</body>
</html>
```